Business Card for a recruitment agency specializing in engineers and geeks.

I am looking to create Business Card Design for my company.
That
## Company name:
Quorvant Inc.
Quorvant is a term coined from the following concepts.
1. geek + engineer
2. geek utopia
## Company Description:
The concept of the company is to be a recruitment agency that creates a paradise for geeky engineers. We want to be a place where engineers can have more freedom and ideal career support.
# Target.
The noun itself is often given to companies that want to hire engineers, geeks, and IT-related personnel, so it would be nice to get the impression that this company seems to have good engineers and IT personnel. There are many occasions where I meet with the human resources department, president, or senior management and give it to them.
# Atmosphere
We are happy with simplicity, but with an impact that will help people remember the company. The logo is based on a dinosaur that does programming, so it should be somewhat playful, but since it will basically be used in a business setting, please don't make it too silly.
# About the logo
See the attached files. The company logo represents our engineers smiling upward because of our work, with the motif of a dinosaur doing programming.
## Color
We will leave the color scheme to you, but since the logo is in black and white, colors with such a taste would fit well.
## file format
ai, psd, png, svg
Industry/Entity Type
human resource and employment agency
Contact Information for Business Card
Company name, address, email, tel, URL,logo
Colors
Designer to choose colors to be used in the design.

```html
<!DOCTYPE html>
<html lang="en">
<head>
<meta charset="utf-8">
<title>Quorvant Business Card</title>
<link href="https://fonts.googleapis.com/css2?family=Outfit:wght@300;400;500;700&display=swap" rel="stylesheet">
<style>
  :root {
    --page: #ffffff;
    --card: #f1f1f3;
    --pattern: #e8e8e9;
    --ink: #111113;
    --ink-soft: #58585b;
  }
  * { margin: 0; padding: 0; box-sizing: border-box; }
  html, body { width: 1200px; height: 1200px; overflow: hidden; }
  body {
    background: var(--page);
    position: relative;
    font-family: "Outfit", sans-serif;
    color: var(--ink);
  }
  .card {
    position: absolute;
    left: 191px;
    width: 826px;
    height: 496px;
    background: var(--card);
    overflow: hidden;
  }
  .card--front { top: 75px; }
  .card--back { top: 604px; }

  .pattern-fill {
    position: absolute;
    inset: 0;
    background: var(--pattern);
  }

  .brand-front {
    position: absolute;
    left: 129px;
    top: 159px;
    display: flex;
    align-items: center;
    gap: 30px;
  }
  .brand-front .brand-square {
    width: 150px;
    height: 150px;
    background: var(--ink);
    border-radius: 10px;
  }
  .brand-front .brand-name {
    font-size: 84px;
    font-weight: 500;
    color: var(--ink-soft);
    letter-spacing: 1px;
    line-height: 1;
  }

  .brand-back {
    position: absolute;
    left: 155px;
    top: 55px;
    width: 156px;
    display: flex;
    flex-direction: column;
    align-items: center;
    gap: 24px;
  }
  .brand-back .brand-square {
    width: 96px;
    height: 96px;
    background: var(--ink);
    border-radius: 8px;
  }
  .brand-back .brand-name {
    font-size: 36px;
    font-weight: 700;
    line-height: 1;
  }

  .contact-list {
    position: absolute;
    left: 67px;
    top: 269px;
    list-style: none;
  }
  .contact-item {
    display: flex;
    align-items: center;
    gap: 12px;
    height: 34px;
    margin-bottom: 10.5px;
    font-size: 25px;
    font-weight: 300;
  }
  .contact-icon { width: 34px; height: 34px; flex: none; }

  .person {
    position: absolute;
    left: 471px;
    top: 195px;
    width: 285px;
    text-align: center;
  }
  .person-name {
    font-size: 47px;
    font-weight: 700;
    letter-spacing: 1.5px;
    line-height: 1.1;
  }
  .person-role {
    font-size: 34px;
    font-weight: 400;
    letter-spacing: 1.5px;
    line-height: 1.2;
    margin-top: 6px;
  }
</style>
</head>
<body>

<section class="card card--front">
  <div class="pattern-fill" role="img" aria-label="Light grey repeating brand pattern covering the card"></div>
  <div class="brand-front">
    <div class="brand-square"></div>
    <span class="brand-name">Quorvant</span>
  </div>
</section>

<section class="card card--back">
  <div class="brand-back">
    <div class="brand-square"></div>
    <span class="brand-name">Quorvant</span>
  </div>

  <ul class="contact-list">
    <li class="contact-item">
      <svg class="contact-icon" viewBox="0 0 34 34">
        <rect x="7" y="7" width="20" height="20" rx="4" transform="rotate(45 17 17)" fill="var(--ink)"/>
        <rect x="10.5" y="12" width="13" height="10" rx="1" fill="none" stroke="#fff" stroke-width="1.8"/>
        <path d="M10.5 12.5 L17 17.5 L23.5 12.5" fill="none" stroke="#fff" stroke-width="1.8"/>
      </svg>
      <span>sample.email@quorvantmail.com</span>
    </li>
    <li class="contact-item">
      <svg class="contact-icon" viewBox="0 0 34 34">
        <rect x="7" y="7" width="20" height="20" rx="4" transform="rotate(45 17 17)" fill="var(--ink)"/>
        <path d="M13 11 l3 0 l1 3.5 l-2 1.5 q1.5 3 4 4 l1.5 -2 l3.5 1 l0 3 q-8 1 -11 -11z" fill="#fff"/>
      </svg>
      <span>+12 34 567890</span>
    </li>
    <li class="contact-item">
      <svg class="contact-icon" viewBox="0 0 34 34">
        <rect x="7" y="7" width="20" height="20" rx="4" transform="rotate(45 17 17)" fill="var(--ink)"/>
        <path d="M10 17 L17 10.5 L24 17" fill="none" stroke="#fff" stroke-width="2"/>
        <rect x="12" y="17" width="10" height="7" fill="#fff"/>
      </svg>
      <span>your address here</span>
    </li>
    <li class="contact-item">
      <svg class="contact-icon" viewBox="0 0 34 34">
        <rect x="7" y="7" width="20" height="20" rx="4" transform="rotate(45 17 17)" fill="var(--ink)"/>
        <path d="M13 10 L13 23 L16 20 L18.5 25 L20.5 24 L18 19 L22 19 Z" fill="#fff"/>
      </svg>
      <span>companyurl.com</span>
    </li>
  </ul>

  <div class="person">
    <div class="person-name">YOUR NAME</div>
    <div class="person-role">Designation</div>
  </div>
</section>

</body>
</html>
```